business card with logo

Would like a business card for an electrical contractor called BRANLOCK ELECTRICS.
No generic electrical imagery (light globe, powerpoints, ect). Would like a logo or symbol created in the design as part of the project . I would like crisp colour. No templated designs like Printvox

is there any other designers willing to submit designs

Electrical

```html
<!DOCTYPE html>
<html lang="en">
<head>
<meta charset="utf-8">
<title>Branlock Electrics – Business Card</title>
<link rel="stylesheet" href="https://fonts.googleapis.com/css2?family=Montserrat:wght@500&family=Arimo:wght@400&display=swap">
<style>
  :root {
    --page-bg: #ffffff;
    --card-bg: #ffffff;
    --card-edge: #b9b9b9;
    --ink: #1a1a1a;
    --orange-light: #f39a2e;
    --orange: #e8642a;
    --orange-deep: #d9352a;
    --white: #ffffff;
  }
  * { margin: 0; padding: 0; box-sizing: border-box; }
  html, body {
    width: 1200px;
    height: 1200px;
    overflow: hidden;
    background: var(--page-bg);
  }
  .canvas {
    position: relative;
    width: 1200px;
    height: 1200px;
  }
  .card {
    position: absolute;
    left: 320px;
    top: 262px;
    width: 595px;
    height: 376px;
    background: var(--card-bg);
    border: 2px solid var(--card-edge);
    border-radius: 9px;
    overflow: hidden;
  }
  .card__divider {
    position: absolute;
    left: 0;
    top: 169px;
    width: 100%;
    height: 4px;
    background: var(--ink);
  }
  .card__band {
    position: absolute;
    left: 0;
    top: 173px;
    width: 100%;
    bottom: 0;
    background:
      linear-gradient(172deg, transparent 62%, rgba(243,154,46,0.85) 70%, transparent 78%),
      linear-gradient(165deg, var(--orange) 0%, var(--orange-deep) 45%, var(--orange) 70%, var(--orange-deep) 100%);
  }

  .card__mark {
    position: absolute;
    left: 284px;
    top: 70px;
    width: 28px;
    height: 28px;
    border-radius: 50%;
    background: var(--orange);
  }
  .card__name,
  .card__trade {
    position: absolute;
    left: 0;
    width: 100%;
    text-align: center;
    font-family: "Montserrat", sans-serif;
    font-weight: 500;
    color: var(--ink);
    line-height: 1;
    white-space: nowrap;
  }
  .card__name {
    top: 124px;
    font-size: 38px;
    letter-spacing: 1px;
  }
  .card__trade {
    top: 180px;
    font-size: 23px;
    letter-spacing: 4px;
  }

  .card__contact {
    position: absolute;
    left: 0;
    width: 100%;
    top: 310px;
    text-align: center;
    font-family: "Arimo", sans-serif;
    font-size: 14px;
    letter-spacing: 1px;
    line-height: 18px;
    color: var(--white);
    white-space: nowrap;
  }

  .footer-mark {
    position: absolute;
    left: 875px;
    width: 260px;
    top: 1066px;
    text-align: center;
    font-family: "Montserrat", sans-serif;
    font-weight: 500;
    color: var(--ink);
    line-height: 1;
  }
  .footer-mark__symbol {
    display: inline-block;
    width: 20px;
    height: 20px;
    margin-bottom: 8px;
    border-radius: 50%;
    background: var(--orange);
  }
  .footer-mark__name { display: block; font-size: 28px; letter-spacing: 1px; }
  .footer-mark__trade { display: block; margin-top: 6px; font-size: 14px; letter-spacing: 3px; }
</style>
</head>
<body>
  <main class="canvas">
    <section class="card" aria-label="Business card front">
      <div class="card__band" role="img" aria-label="Flowing orange and red wave background"></div>
      <div class="card__divider"></div>
      <span class="card__mark"></span>
      <span class="card__name">BRANLOCK</span>
      <span class="card__trade">ELECTRICS</span>
      <p class="card__contact">
        Hollis Bay, Westmere, 48 Harlow Road<br>
        ph: 555-214-3870; Fax: 555-214-3871
      </p>
    </section>

    <div class="footer-mark">
      <span class="footer-mark__symbol"></span>
      <span class="footer-mark__name">BRANLOCK</span>
      <span class="footer-mark__trade">ELECTRICS</span>
    </div>
  </main>
</body>
</html>
```